Tallowbrook Fitness - Personal & Rehab Training

Business Card for my personal training business - Tallowbrook Fitness. I focus on personal and rehab training. I would like a double sided card, round edges. front of card will be my existing logo and the back will have an image (black and white or exercise, people exercising, weights, etc) along with my name and details. Such as:
Corisse Pembly
Personal & Rehab Trainer
www.tallowbrookfitness.com.au
0438264905
I have some images that I have downloaded that I am happy to send to the designer.
Thanks
Target Market(s)
athletes, middle to high income, sport related
Contact Information for Business Card
Corisse Pembly
Personal & Rehab Trainer
0438264905
Colors
Designer to choose only greyscale colors for use in the design.
Requirements
Must have
- my existing logo
Nice to have
- one of the images uploaded. I really like the girl with the mint coloured shoes as this is one of my logo colours

```html
<!DOCTYPE html>
<html lang="en">
<head>
<meta charset="utf-8">
<title>Tallowbrook Fitness – Business Card</title>
<link rel="stylesheet" href="https://fonts.googleapis.com/css2?family=Montserrat:wght@400;600;700&display=swap">
<style>
  :root {
    --page: #1b1b1c;
    --card: #252628;
    --card-pattern-a: #27282a;
    --card-pattern-b: #2d2e31;
    --mint: #8fd3a0;
    --white: #f4f4f4;
    --rule: #8a8a8a;
  }
  * { box-sizing: border-box; margin: 0; padding: 0; }
  html, body {
    width: 1200px; height: 1108px; overflow: hidden;
    background: var(--page);
    font-family: "Montserrat", Arial, sans-serif;
  }
  .card {
    position: absolute;
    width: 400px; height: 640px;
    border-radius: 30px;
    background: var(--card);
    overflow: hidden;
    box-shadow: 0 18px 40px rgba(0,0,0,.45);
  }
  .card--front { left: 160px; top: 200px; }
  .card--back  { left: 640px; top: 268px; }

  .brand { position: absolute; display: flex; align-items: center; gap: 18px; }
  .brand__square {
    width: 64px; height: 64px; flex: none;
    border: 4px solid var(--mint); border-radius: 10px;
  }
  .brand__name {
    color: var(--white); font-weight: 600; letter-spacing: .14em;
    text-transform: uppercase; line-height: 1.15;
    padding-bottom: 10px; border-bottom: 2px solid var(--white);
  }
  .card--front .brand { left: 40px; top: 96px; }
  .card--front .brand__name { font-size: 20px; }

  .contact {
    position: absolute; left: 0; right: 0; bottom: 70px;
    text-align: center; color: var(--white);
  }
  .contact__name {
    color: var(--mint); font-weight: 700; font-size: 30px;
    text-transform: uppercase; letter-spacing: .02em;
  }
  .contact__role {
    font-size: 19px; text-transform: uppercase; margin-top: 6px; letter-spacing: .02em;
  }
  .contact__rule {
    width: 160px; height: 1px; background: var(--rule); margin: 26px auto 20px;
  }
  .contact__phone { font-size: 26px; letter-spacing: .03em; }
  .contact__web { font-size: 16px; text-transform: uppercase; margin-top: 12px; }
  .contact__web span { color: var(--mint); }

  .card__backdrop {
    position: absolute; inset: 0;
    background: linear-gradient(160deg, var(--card-pattern-b), var(--card-pattern-a) 70%);
  }
  .card--back .brand {
    left: 40px; right: 40px; bottom: 70px;
    flex-direction: column; align-items: stretch; gap: 26px;
  }
  .card--back .brand__square { align-self: center; margin-left: 110px; width: 60px; height: 60px; }
  .card--back .brand__name { display: block; font-size: 27px; }
</style>
</head>
<body>
  <section class="card card--front" aria-label="Card front">
    <div class="brand">
      <span class="brand__square"></span>
      <span class="brand__name">Tallowbrook<br>Fitness</span>
    </div>
    <div class="contact">
      <p class="contact__name">Corisse Pembly</p>
      <p class="contact__role">Personal &amp; Rehab Trainer</p>
      <div class="contact__rule"></div>
      <p class="contact__phone">0438264905</p>
      <p class="contact__web">www.<span>tallowbrookfitness.com.au</span></p>
    </div>
  </section>

  <section class="card card--back" aria-label="Card back">
    <div class="card__backdrop" role="img" aria-label="Faint repeating brand pattern across the card"></div>
    <div class="brand">
      <span class="brand__square"></span>
      <span class="brand__name">Tallowbrook<br>Fitness</span>
    </div>
  </section>
</body>
</html>
```